Business card for Sports Apparel business

DOUBLE SIDED DESIGN
We need business cards for a new sports apparel business. We are developing a protective headband for soccer initially.
Corvell is focused on designing and developing head protection products to reduce the likelihood of concussion when playing sports. Exploring and understanding medical insights, material science research, current and former players experiences and governing bodies guidelines has allowed Corvell to develop the safety, style, form and function requirements of a suitable product to bring to market.
Target Market(s)
Mums buying kits for the sons and daughters. Amateur footballers.
Industry/Entity Type
Sporting Good
Contact Information for Business Card
Martin Ashgrove - CEO
Mobile: +44 7391608254
Email: martin@corvell.co.uk
Tel: 0208 5143927
Helena Pardoe - COO
Mob: +44 7356 409183
Email: helena@corvell.co.uk
Tel: 0208 5143927
Duncan Wyvern - CCO
Mob: +44 7468 230517
Email: duncan@corvell.co.uk
Tel: 0208 5143927
Look and feel

```html
<!DOCTYPE html>
<html lang="en">
<head>
<meta charset="UTF-8">
<title>Corvell Business Card</title>
<link rel="stylesheet" href="https://fonts.googleapis.com/css2?family=Montserrat:wght@400;500;600&display=swap">
<style>
  :root {
    --brand-blue: #0f5a94;
    --brand-blue-deep: #0b4a7c;
    --ink: #4a4a4a;
    --ink-soft: #6d6d6d;
    --paper: #ffffff;
    --paper-shade: #eeeeee;
    --wedge-grey: #8a8a8a;
    --backdrop: #d9dcdf;
  }
  * { box-sizing: border-box; margin: 0; padding: 0; }
  html, body { width: 1200px; height: 900px; overflow: hidden; }
  body {
    background: var(--backdrop);
    font-family: "Montserrat", sans-serif;
    display: flex;
    flex-direction: column;
    align-items: center;
    justify-content: center;
    gap: 34px;
  }
  .card {
    position: relative;
    width: 700px;
    height: 400px;
    overflow: hidden;
    box-shadow: 0 6px 18px rgba(0,0,0,0.18);
  }
  /* Front */
  .card-front {
    background: linear-gradient(135deg, var(--paper-shade) 0%, var(--paper) 45%, var(--paper) 100%);
  }
  .accent-tab {
    position: absolute;
    left: 0; top: 52px;
    width: 12px; height: 56px;
    background: var(--brand-blue);
  }
  .bottom-band {
    position: absolute;
    left: 0; bottom: 0;
    width: 340px; height: 60px;
  }
  .holder { position: absolute; left: 48px; top: 56px; }
  .holder-name {
    color: var(--brand-blue);
    font-weight: 600;
    font-size: 22px;
    letter-spacing: 0.5px;
    text-transform: uppercase;
  }
  .holder-role {
    color: var(--ink-soft);
    font-size: 16px;
    font-weight: 400;
    margin-top: 2px;
  }
  .divider {
    position: absolute;
    left: 36px; top: 138px;
    width: 600px; height: 2px;
    background: var(--brand-blue);
  }
  .phones {
    position: absolute;
    left: 36px; top: 158px;
    list-style: none;
    color: var(--ink-soft);
    font-size: 17px;
    line-height: 28px;
  }
  .phones li, .online li { display: flex; align-items: center; gap: 10px; }
  .icon { width: 16px; height: 16px; flex: none; }
  .wordmark {
    position: absolute;
    right: 64px; top: 62px;
    display: flex;
    align-items: center;
    gap: 14px;
  }
  .wordmark-square {
    width: 22px; height: 22px;
    background: var(--brand-blue);
  }
  .wordmark-name {
    font-weight: 600;
    font-size: 46px;
    letter-spacing: 2px;
    color: var(--ink);
    text-transform: uppercase;
  }
  .online {
    position: absolute;
    right: 60px; bottom: 38px;
    list-style: none;
    color: var(--ink-soft);
    font-size: 17px;
    line-height: 28px;
    text-align: right;
  }
  .online li { justify-content: flex-end; }
  /* Back */
  .card-back {
    background: linear-gradient(160deg, var(--brand-blue) 0%, var(--brand-blue-deep) 100%);
    display: flex;
    align-items: center;
    justify-content: center;
    gap: 20px;
  }
  .card-back .wordmark-square {
    width: 30px; height: 30px;
    background: var(--paper);
  }
  .card-back .wordmark-name {
    color: var(--paper);
    font-size: 72px;
    letter-spacing: 3px;
  }
</style>
</head>
<body>

  <section class="card card-front" aria-label="Business card front">
    <div class="accent-tab"></div>

    <svg class="bottom-band" viewBox="0 0 340 60" aria-hidden="true">
      <polygon points="0,0 260,0 240,60 0,60" fill="var(--brand-blue)"/>
      <polygon points="260,0 340,0 340,60 240,60" fill="var(--wedge-grey)" opacity="0.55"/>
    </svg>

    <div class="holder">
      <p class="holder-name">Martin Ashgrove</p>
      <p class="holder-role">CEO</p>
    </div>

    <div class="divider"></div>

    <ul class="phones">
      <li>
        <svg class="icon" viewBox="0 0 16 16" aria-hidden="true"><path d="M4 1.5 6 4.5 4.8 6.2c.8 1.7 2.3 3.2 4 4L10.5 9l3 2-1 2.5c-5 .5-10.5-5-10-10Z" fill="var(--brand-blue)"/></svg>
        0208 5143927
      </li>
      <li>
        <svg class="icon" viewBox="0 0 16 16" aria-hidden="true"><rect x="4" y="1" width="8" height="14" rx="1.5" fill="none" stroke="var(--brand-blue)" stroke-width="1.6"/><circle cx="8" cy="12.3" r="0.9" fill="var(--brand-blue)"/></svg>
        +44 7391608254
      </li>
    </ul>

    <div class="wordmark">
      <span class="wordmark-square"></span>
      <span class="wordmark-name">Corvell</span>
    </div>

    <ul class="online">
      <li>
        martin@corvell.co.uk
        <svg class="icon" viewBox="0 0 16 16" aria-hidden="true"><rect x="1.5" y="3.5" width="13" height="9" fill="none" stroke="var(--brand-blue)" stroke-width="1.5"/><path d="M1.5 3.5 8 9l6.5-5.5" fill="none" stroke="var(--brand-blue)" stroke-width="1.5"/></svg>
      </li>
      <li>
        www.corvell.co.uk
        <svg class="icon" viewBox="0 0 16 16" aria-hidden="true"><circle cx="8" cy="8" r="6.5" fill="none" stroke="var(--brand-blue)" stroke-width="1.4"/><ellipse cx="8" cy="8" rx="2.8" ry="6.5" fill="none" stroke="var(--brand-blue)" stroke-width="1.2"/><path d="M1.5 8h13M2.6 4.8h10.8M2.6 11.2h10.8" stroke="var(--brand-blue)" stroke-width="1.1"/></svg>
      </li>
    </ul>
  </section>

  <section class="card card-back" aria-label="Business card back">
    <span class="wordmark-square"></span>
    <span class="wordmark-name">Corvell</span>
  </section>

</body>
</html>
```